Harrowvane Business Card

Looking for a new business Card layout for our company, harrowvane.

Standard Business Card , Name, email, phone, website. www.harrowvane.com

```html
<!DOCTYPE html>
<html lang="en">
<head>
<meta charset="utf-8">
<title>Harrowvane Business Card</title>
<link href="https://fonts.googleapis.com/css2?family=Roboto:wght@300;400;700&display=swap" rel="stylesheet">
<style>
  :root {
    --bg: #2b2b2c;
    --card: #1f1f20;
    --blue: #3fb3de;
    --white: #ffffff;
    --grey: #c9c9c9;
  }
  * { margin: 0; padding: 0; box-sizing: border-box; }
  html, body {
    width: 1200px; height: 901px; overflow: hidden;
    background: var(--bg);
    font-family: "Roboto", Arial, sans-serif;
  }
  .card {
    position: absolute;
    width: 620px; height: 354px;
    background: var(--card);
    box-shadow: 0 14px 30px rgba(0,0,0,.45);
  }
  .card--front { left: 480px; top: 50px; }
  .card--back { left: 120px; top: 470px; }

  .wordmark {
    display: flex; align-items: center; gap: 12px;
    font-weight: 700; color: var(--blue);
    letter-spacing: 1px; text-transform: uppercase;
    white-space: nowrap;
  }
  .wordmark__dot {
    width: 20px; height: 20px; border-radius: 50%;
    background: var(--blue); flex: none;
  }
  .card--front .wordmark {
    position: absolute; left: 0; right: 0; top: 130px;
    justify-content: center; font-size: 44px; line-height: 1;
  }
  .card--front .website {
    position: absolute; left: 0; right: 0; top: 236px;
    text-align: center; font-size: 17px; font-weight: 300;
    color: var(--white); letter-spacing: .5px;
  }
  .accent { color: var(--blue); }

  .person { position: absolute; left: 44px; top: 48px; }
  .person__name { font-size: 27px; font-weight: 400; color: var(--blue); }
  .person__role { font-size: 19px; font-weight: 300; color: var(--grey); margin-top: 2px; }

  .contacts { position: absolute; left: 44px; bottom: 40px; list-style: none; }
  .contacts li {
    display: flex; align-items: center; gap: 14px;
    font-size: 19px; font-weight: 300; color: var(--white);
    margin-top: 8px; line-height: 1.2;
  }
  .contacts svg { width: 18px; height: 18px; flex: none; }

  .card--back .wordmark {
    position: absolute; right: 40px; top: 165px;
    font-size: 36px; line-height: 1;
  }
</style>
</head>
<body>
  <section class="card card--front">
    <div class="wordmark"><span class="wordmark__dot"></span>Harrowvane</div>
    <p class="website">www.<span class="accent">harrowvane</span>.com</p>
  </section>

  <section class="card card--back">
    <div class="person">
      <h1 class="person__name">Daniel Morrow</h1>
      <p class="person__role">Manager</p>
    </div>

    <div class="wordmark"><span class="wordmark__dot"></span>Harrowvane</div>

    <ul class="contacts">
      <li>
        <svg viewBox="0 0 24 24" fill="#3fb3de"><path d="M6.6 10.8a15.1 15.1 0 0 0 6.6 6.6l2.2-2.2a1 1 0 0 1 1-.25 11.4 11.4 0 0 0 3.6.57 1 1 0 0 1 1 1V20a1 1 0 0 1-1 1A17 17 0 0 1 3 4a1 1 0 0 1 1-1h3.5a1 1 0 0 1 1 1c0 1.25.2 2.45.57 3.57a1 1 0 0 1-.25 1z"/></svg>
        123-456-7800
      </li>
      <li>
        <svg viewBox="0 0 24 24" fill="none" stroke="#3fb3de" stroke-width="2"><rect x="3" y="5" width="18" height="14" rx="1"/><path d="M3 6l9 7 9-7"/></svg>
        daniel@harrowvane.com
      </li>
      <li>
        <svg viewBox="0 0 24 24" fill="none" stroke="#3fb3de" stroke-width="1.8"><circle cx="12" cy="12" r="9"/><ellipse cx="12" cy="12" rx="4" ry="9"/><path d="M3 12h18M5 7h14M5 17h14"/></svg>
        <span>www.<span class="accent">harrowvane</span>.com</span>
      </li>
    </ul>
  </section>
</body>
</html>
```